Retail Jewelry Business Card Design Project

We are in need of a new business card design for a retail jewelry store. This store is in the business of fine jewelry including but not specific to bridal jewelry, diamonds, designer jewelry and watches.

This store has been in business for 20 years but continues to strive for a modern professional appeal. The main colors use for this business are a royal blue, white and silver.

Target Market(s)

Target market is ages 18-50

Industry/Entity Type

Jewelry

Requirements
Must have
• Sales Person Name
Sales Person Email Address

Store Address
Store Phone
Website

Standard business card size. No odd shapes or sizes.
Nice to have
• Overall modern feel for card.

We have thought that a design with a nice feature of the logo on the back of the card would be nice but open to ideas.
Should not have
• No specific images of jewelry should be used.

```html
<!DOCTYPE html>
<html lang="en">
<head>
<meta charset="utf-8">
<title>Marlowe Hart Fine Jewelry – Business Cards</title>
<link rel="stylesheet" href="https://fonts.googleapis.com/css2?family=Source+Sans+3:wght@400;600;700&display=swap">
<style>
  :root {
    --indigo: #23106b;
    --violet: #5e3f9e;
    --lavender: #a996d0;
    --mist: #e6def1;
    --ink: #1c1c1c;
    --paper: #ffffff;
    --edge: #111111;
  }
  * { box-sizing: border-box; margin: 0; padding: 0; }
  html, body { width: 1200px; height: 693px; overflow: hidden; background: var(--paper); }
  body { font-family: "Source Sans 3", sans-serif; }

  .canvas {
    position: relative;
    width: 1200px;
    height: 693px;
    display: flex;
    align-items: center;
    justify-content: center;
    gap: 60px;
  }
  .card {
    position: relative;
    width: 480px;
    height: 320px;
  }
  .card-art { position: absolute; inset: 0; width: 100%; height: 100%; }

  .brand-name {
    position: absolute;
    left: 0; right: 0;
    top: 112px;
    text-align: center;
    color: var(--violet);
    font-weight: 600;
    font-size: 40px;
    letter-spacing: 0.5px;
    line-height: 1.1;
  }
  .brand-name span { display: block; font-size: 22px; letter-spacing: 4px; text-transform: uppercase; }

  .card-url {
    position: absolute;
    right: 20px;
    bottom: 22px;
    color: var(--paper);
    font-size: 8px;
    font-weight: 400;
  }

  .contact-block {
    position: absolute;
    left: 36px;
    top: 96px;
    color: var(--ink);
  }
  .contact-name { font-size: 24px; font-weight: 700; margin-bottom: 10px; }
  .contact-line { font-size: 13px; line-height: 1.3; }

  .corner-name {
    position: absolute;
    right: 22px;
    top: 78px;
    color: var(--violet);
    font-size: 14px;
    font-weight: 600;
    text-align: center;
    line-height: 1.05;
  }
  .corner-name span { display: block; font-size: 8px; letter-spacing: 1.5px; text-transform: uppercase; }
</style>
</head>
<body>
<main class="canvas">

  <!-- Front -->
  <section class="card card-front">
    <svg class="card-art" viewBox="0 0 480 320" aria-hidden="true">
      <defs>
        <linearGradient id="paperFront" x1="0" y1="0" x2="1" y2="1">
          <stop offset="0.45" stop-color="#ffffff"/>
          <stop offset="1" stop-color="#d9cde9"/>
        </linearGradient>
        <linearGradient id="swooshFront" x1="0" y1="0" x2="1" y2="0">
          <stop offset="0" stop-color="#b9a8da"/>
          <stop offset="0.6" stop-color="#6d52ad"/>
          <stop offset="1" stop-color="#ece6f4"/>
        </linearGradient>
        <linearGradient id="bandFront" x1="0" y1="0" x2="1" y2="0">
          <stop offset="0" stop-color="#8e76c2"/>
          <stop offset="0.55" stop-color="#3c2287"/>
          <stop offset="1" stop-color="#1e0b63"/>
        </linearGradient>
        <clipPath id="cardClipFront"><rect x="1" y="1" width="478" height="318" rx="18"/></clipPath>
        <clipPath id="stripeClipFront"><path d="M0,0 L150,0 C70,20 15,60 0,100 Z"/></clipPath>
      </defs>
      <g clip-path="url(#cardClipFront)">
        <rect width="480" height="320" fill="url(#paperFront)"/>
        <g clip-path="url(#stripeClipFront)" stroke="#7b62b6" stroke-width="3.5">
          <line x1="0" y1="6" x2="160" y2="6"/><line x1="0" y1="14" x2="160" y2="14"/>
          <line x1="0" y1="22" x2="160" y2="22"/><line x1="0" y1="30" x2="160" y2="30"/>
          <line x1="0" y1="38" x2="160" y2="38"/><line x1="0" y1="46" x2="160" y2="46"/>
          <line x1="0" y1="54" x2="160" y2="54"/><line x1="0" y1="62" x2="160" y2="62"/>
          <line x1="0" y1="70" x2="160" y2="70"/><line x1="0" y1="78" x2="160" y2="78"/>
          <line x1="0" y1="86" x2="160" y2="86"/><line x1="0" y1="94" x2="160" y2="94"/>
        </g>
        <path d="M0,155 C20,65 120,8 300,0 L150,0 C70,20 15,60 0,100 Z" fill="url(#swooshFront)"/>
        <path d="M0,155 C20,65 120,8 300,0" fill="none" stroke="var(--indigo)" stroke-width="2"/>
        <rect x="0" y="252" width="480" height="3" fill="var(--indigo)"/>
        <rect x="0" y="255" width="480" height="4" fill="#ffffff"/>
        <rect x="0" y="259" width="480" height="61" fill="url(#bandFront)"/>
        <path d="M0,266 C120,258 260,262 330,290 L0,300 Z" fill="#ffffff" opacity="0.15"/>
      </g>
      <rect x="1" y="1" width="478" height="318" rx="18" fill="none" stroke="var(--edge)" stroke-width="2"/>
    </svg>
    <h1 class="brand-name">Marlowe Hart<span>Fine Jewelry</span></h1>
    <p class="card-url">www.marlowehartjewelry.com</p>
  </section>

  <!-- Back -->
  <section class="card card-back">
    <svg class="card-art" viewBox="0 0 480 320" aria-hidden="true">
      <defs>
        <linearGradient id="paperBack" x1="0" y1="0" x2="1" y2="1">
          <stop offset="0.45" stop-color="#ffffff"/>
          <stop offset="1" stop-color="#d9cde9"/>
        </linearGradient>
        <linearGradient id="swooshBack" x1="0" y1="0" x2="1" y2="0">
          <stop offset="0" stop-color="#b9a8da"/>
          <stop offset="0.6" stop-color="#6d52ad"/>
          <stop offset="1" stop-color="#ece6f4"/>
        </linearGradient>
        <linearGradient id="bandBack" x1="0" y1="0" x2="1" y2="0">
          <stop offset="0" stop-color="#8e76c2"/>
          <stop offset="0.55" stop-color="#3c2287"/>
          <stop offset="1" stop-color="#1e0b63"/>
        </linearGradient>
        <clipPath id="cardClipBack"><rect x="1" y="1" width="478" height="318" rx="18"/></clipPath>
        <clipPath id="stripeClipBack"><path d="M0,0 L110,0 C55,12 15,35 0,60 Z"/></clipPath>
      </defs>
      <g clip-path="url(#cardClipBack)">
        <rect width="480" height="320" fill="url(#paperBack)"/>
        <g clip-path="url(#stripeClipBack)" stroke="#7b62b6" stroke-width="3.5">
          <line x1="0" y1="6" x2="120" y2="6"/><line x1="0" y1="14" x2="120" y2="14"/>
          <line x1="0" y1="22" x2="120" y2="22"/><line x1="0" y1="30" x2="120" y2="30"/>
          <line x1="0" y1="38" x2="120" y2="38"/><line x1="0" y1="46" x2="120" y2="46"/>
          <line x1="0" y1="54" x2="120" y2="54"/>
        </g>
        <path d="M0,90 C40,35 160,6 380,0 L110,0 C55,12 15,35 0,60 Z" fill="url(#swooshBack)"/>
        <path d="M0,90 C40,35 160,6 380,0" fill="none" stroke="var(--indigo)" stroke-width="2"/>
        <rect x="0" y="252" width="480" height="3" fill="var(--indigo)"/>
        <rect x="0" y="255" width="480" height="4" fill="#ffffff"/>
        <rect x="0" y="259" width="480" height="61" fill="url(#bandBack)"/>
        <path d="M0,266 C120,258 260,262 330,290 L0,300 Z" fill="#ffffff" opacity="0.15"/>
      </g>
      <rect x="1" y="1" width="478" height="318" rx="18" fill="none" stroke="var(--edge)" stroke-width="2"/>
    </svg>
    <p class="corner-name">Marlowe Hart<span>Fine Jewelry</span></p>
    <div class="contact-block">
      <h2 class="contact-name">Marlowe Hart Fine</h2>
      <p class="contact-line">2280 Lindell Street</p>
      <p class="contact-line">Bayport, FL 32500</p>
      <p class="contact-line">Email: marlowe@marlowehartjewelry.com</p>
      <p class="contact-line">www.marlowehartjewelry.com</p>
    </div>
    <p class="card-url">www.marlowehartjewelry.com</p>
  </section>

</main>
</body>
</html>
```